Thornbury Cleaning – Website Redesign (Clean, Modern, Trust-Focused)

Thornbury Cleaning — Homepage Redesign Brief

Project Goal

We need a complete redesign of the homepage for our cleaning business, Thornbury Cleaning.
The goal is a clean, modern, trust-building homepage that works equally well for:
• Residential clients
• Commercial clients

The page should feel polished, reliable, easy to navigate, and completely free from clutter, gimmicks, or corporate-sounding fluff.

About Us (Context)

Thornbury Cleaning has operated in Sale, Victoria for over 30 years.
Our brand is built on:
• Reliability
• Convenience
• Long-term trust
• Straightforward, no-nonsense communication

We do not want to look like a large franchise, and we do not want to look cute or playful.
The design must feel modern, practical, confident, and professional.

What We Need Designed — Homepage Only

1. Hero Section

A clean, modern hero area with:
• A simple image or clean background (no clutter, no heavy overlays).
Images from our current site may be helpful, or you may source alternatives.
• Headline suggestion (designer may refine):
“30+ Years of Commercial and Residential Cleaning in Sale”
• Sub-headline suggestion:
“Trusted by locals for three decades.”
• Primary CTA button: Get a Quote

2. Trust-Building Logos

Positioned directly beneath the hero:
• Small, neat logos of organisations we work with
(RLK, Bramwell, Eastvale Regional Care, OPM, etc.)
• A clean ReviewHub Reviews block (stars + review count)
• Must be compact, tidy, evenly spaced — not loud or oversized

3. Trust Block / Problem–Solution Copy

This section introduces why hiring cleaners can be stressful and why reliability matters.

Headline example:
“Call the cleaners you can count on.”

We have existing copy for this section.
Please present it in a minimal, breathable, modern layout that is easy to scan.

4. Stats / Counters Section

Three sharp, structured stat boxes:
• 92+ Recurring Clients
• 4,150+ Visits Per Year
• 265+ Pre-Sale / Exit Cleans

These should look clean and understated — not oversized or gimmicky.

5. Values Section

A short section featuring our core values:
• Be Real
• Do It Right
• Have Fun
• Make It Easy

Designer has flexibility with layout.
(Sections 5 and 6 may swap depending on what flows better.)

6. Services Preview

A simple grid or row with links to our main services:
• Commercial Cleaning
• Residential Cleaning
• Window Cleaning
• Steam Cleaning

Small icons or photos are fine — but no clip art or cartoon-style graphics.

7. Footer

A very clean, simple footer with contact details.
No clutter, no heavy visual styling.

Style Requirements

Overall Tone
• Clean
• Modern
• Minimal
• Trust-driven
• Easy to read and navigate

Do NOT use
• Clip art
• Cute or playful icons
• Flowers, sparkles, “feminine” cleaning imagery
• Heavy or overly bold corporate fonts
• Busy backgrounds
• Long paragraphs of text

Reference Material

Current Website (for copy + structure only)

https://thornburycleaning-example.com.au

Rough Canva Mock-Up (layout inspiration only)

(We will upload this separately. It’s not a final design — just a loose concept for spacing/flow.)

Logo

Please use the new Thornbury Cleaning logo (uploaded in files) or a placeholder if needed. Attached is a potential for a new logo or site colours not wedded to the idea though.

What the Homepage Should Communicate

Within seconds, a visitor should understand that:
• We are established
• We are local
• We are reliable
• We make cleaning easy
• Getting a quote is quick and simple

The homepage should feel effortless, trustworthy, and modern.

Deliverable

A complete homepage design layout suitable for WordPress.
Figma, Adobe XD, or a similar design tool is fine.

Target Market(s)

Residential and commercial clients in Sale, Victoria and surrounding Gippsland region. Typical clients include busy households, office managers, receptionists, medical centres, community organisations, local businesses, and real estate/property professionals. Clients value reliability, simplicity, and stress-free long-term cleaning support.

Industry/Entity Type

Cleaning services (Residential & Commercial)

Font styles to use
Sans Serif

Requirements
Must have
• • Clean, modern, minimal layout • A trust-driven design that highlights proof (logos, stats, reviews) near the top • Clear hierarchy and no clutter • A strong hero section with simple messaging and a clear CTA • Trust logos + ReviewHub Reviews block directly under the hero • Structured stats/counters section • Values section (Be Real, Do It Right, Have Fun, Make It Easy) • Services preview (Commercial, Residential, Window, Steam/Carpet) • Clean footer with contact details • Use our new Thornbury Cleaning logo (or placeholder if needed) • Easy-to-read typography and spacing • Must feel like a local, real cleaning business — not a franchise
Nice to have
• • An option with centred hero text and an option with left-aligned text • Option to preview hero section with or without a quote form • Subtle use of the navy + gold palette (not heavy or corporate) • Soft, minimal background images (not busy city skylines) • Subtle section dividers or whitespace breaks to improve flow • Slightly rounded card corners for a friendly but still modern feel
Should not have
• • No clip-art, cartoon mops, sparkles, bubbles, or generic cleaning icons • No overly bold, blocky, or corporate fonts • No “mega-city” skylines (we are a regional/rural business) • No heavy overlays, dark gradients, or cluttered hero images • No long paragraphs or dense text blocks • No template-style designs that look generic or AI-generated • No overly feminine, overly masculine, or overly playful designs • No neon colors or high-saturation palettes

```html
<!DOCTYPE html>
<html lang="en">
<head>
<meta charset="utf-8">
<title>Thornbury Cleaning – Commercial and Residential Cleaning in Sale</title>
<link rel="stylesheet" href="https://fonts.googleapis.com/css2?family=Montserrat:wght@500;600;700;800&family=Open+Sans:wght@400;600&display=swap">
<style>
:root{
  --navy:#16294a;
  --navy-deep:#0f1f3a;
  --gold:#c9a24a;
  --gold-soft:#e7d4a3;
  --ink:#1d2433;
  --muted:#6b7280;
  --line:#e5e7eb;
  --paper:#ffffff;
  --mist:#f5f6f8;
}
*{box-sizing:border-box;margin:0;padding:0}
html,body{width:1200px;height:3140px;overflow:hidden}
body{background:var(--paper);font-family:"Open Sans",Arial,sans-serif;color:var(--ink);font-size:13px;line-height:1.6}
h1,h2,h3,.heading{font-family:"Montserrat",Arial,sans-serif}
.eyebrow{font-family:"Montserrat",Arial,sans-serif;font-weight:700;font-size:11px;letter-spacing:2px;color:var(--gold);text-transform:uppercase}
.btn{display:inline-block;font-family:"Montserrat",Arial,sans-serif;font-weight:700;font-size:12px;letter-spacing:1px;text-transform:uppercase;text-decoration:none}
.btn-gold{background:var(--gold);color:#fff;padding:14px 26px;border-radius:4px}
.btn-outline{border:1.5px solid var(--gold);color:var(--gold);padding:8px 18px;border-radius:3px;font-size:10px}

/* Hero */
.hero{position:relative;height:660px;overflow:hidden;color:#fff}
.hero-photo{position:absolute;inset:0;background:linear-gradient(100deg,#1b2230 0%,#2f3846 38%,#6f7a86 62%,#aeb6bd 82%,#d7dbde 100%)}
.nav{position:absolute;top:0;left:0;right:0;height:80px;display:flex;align-items:center;padding:0 60px;gap:40px}
.brand{display:flex;align-items:center;gap:10px;font-family:"Montserrat",Arial,sans-serif;font-weight:800;font-size:19px;color:#fff;letter-spacing:.5px;white-space:nowrap}
.brand-dot{width:14px;height:14px;border-radius:50%;background:var(--gold)}
.menu{display:flex;gap:26px;list-style:none;margin-left:30px}
.menu a{font-family:"Montserrat",Arial,sans-serif;font-weight:600;font-size:11px;letter-spacing:1px;color:#fff;text-decoration:none;text-transform:uppercase;white-space:nowrap}
.menu a.active{color:var(--gold);border-bottom:2px solid var(--gold);padding-bottom:4px}
.nav-call{margin-left:auto;display:flex;align-items:center;gap:10px}
.nav-call .ico{width:34px;height:34px;border-radius:50%;background:var(--gold);display:flex;align-items:center;justify-content:center}
.nav-call small{display:block;font-size:9px;letter-spacing:1px;color:var(--gold-soft);text-transform:uppercase;font-family:"Montserrat",Arial,sans-serif;font-weight:600}
.nav-call strong{font-family:"Montserrat",Arial,sans-serif;font-size:14px}
.hero-copy{position:absolute;left:60px;top:215px;width:560px}
.hero-copy h1{font-size:50px;line-height:1.08;font-weight:800;text-transform:uppercase;margin:14px 0 18px}
.hero-copy p{font-size:14px;color:#dfe3e8;max-width:480px;margin-bottom:30px}
.hero-actions{display:flex;align-items:center;gap:28px}
.rating{display:flex;align-items:center;gap:10px;background:#fff;color:var(--ink);padding:8px 14px;border-radius:6px}
.rating-mark{width:28px;height:28px;border-radius:50%;background:var(--navy)}
.rating .stars{display:flex;gap:2px}
.rating b{display:block;font-family:"Montserrat",Arial,sans-serif;font-size:10px;letter-spacing:.5px}

/* Partners */
.partners{height:120px;border-bottom:1px solid var(--line);text-align:center;padding-top:22px}
.partners .label{font-size:10px;color:var(--muted);letter-spacing:1px;margin-bottom:14px}
.partner-row{display:flex;justify-content:center;gap:44px;align-items:center}
.partner{font-family:"Montserrat",Arial,sans-serif;font-weight:700;font-size:13px;color:#a7adb6}

/* Trust */
.trust{text-align:center;padding-top:56px;height:600px}
.trust h2{font-size:36px;font-weight:800;color:var(--navy);text-transform:uppercase;line-height:1.15;margin:10px 0 18px}
.trust .lead{width:700px;margin:0 auto 14px;color:#4b5563}
.trust .note{font-size:12px;color:var(--muted);margin-bottom:28px}
.stats{display:flex;justify-content:center;gap:28px}
.stat{width:270px;background:#fff;border:1px solid var(--line);border-radius:8px;box-shadow:0 8px 24px rgba(22,41,74,.08);padding:22px 24px 22px;text-align:center;display:flex;flex-direction:column;align-items:center}
.stat .ico{width:50px;height:50px;border-radius:50%;background:var(--gold);display:flex;align-items:center;justify-content:center;margin-bottom:10px}
.stat h3{font-size:12px;font-weight:700;color:var(--navy);letter-spacing:1px;text-transform:uppercase}
.stat .num{font-family:"Montserrat",Arial,sans-serif;font-size:34px;font-weight:800;color:var(--gold);line-height:1.15}
.stat p{font-size:11px;color:var(--muted);margin-top:6px;line-height:1.5}

.band-photo{height:280px;position:relative}
.band-photo.cleaner{background:linear-gradient(180deg,#ffffff 0%,#e7eaee 18%,#b9c2cc 55%,#8e99a6 100%)}
.band-photo.vans{height:320px;background:linear-gradient(180deg,#cfd8e2 0%,#e9edf1 45%,#bfc6cc 75%,#8f979e 100%)}

/* Services */
.services{text-align:center;padding-top:40px;height:580px}
.services h2,.values h2{font-size:34px;font-weight:800;color:var(--navy);text-transform:uppercase;line-height:1.15;margin-top:8px}
.cards{display:flex;justify-content:center;gap:20px;margin-top:30px}
.card{width:222px;height:420px;background:#fff;border:1px solid var(--line);border-radius:6px;box-shadow:0 6px 18px rgba(22,41,74,.08);overflow:hidden;position:relative}
.card .thumb{height:170px;background:linear-gradient(160deg,#c3ccd5,#8e9aa7)}
.card .thumb.home{background:linear-gradient(160deg,#e4dccb,#b9a98a)}
.card .thumb.window{background:linear-gradient(160deg,#b8c6d2,#6f7f8f)}
.card .thumb.steam{background:linear-gradient(160deg,#a6aeb4,#5c646b)}
.card .badge{width:52px;height:52px;border-radius:50%;background:var(--gold);border:3px solid #fff;position:absolute;top:144px;left:85px;display:flex;align-items:center;justify-content:center}
.card h3{font-size:13px;font-weight:800;color:var(--navy);text-transform:uppercase;margin:40px 0 8px}
.card p{font-size:11px;color:var(--muted);padding:0 18px;height:112px}
.card.featured{background:var(--navy);border-color:var(--navy)}
.card.featured h3{color:#fff}
.card.featured p{color:#c7cfdb}

/* Values */
.values{text-align:center;padding-top:10px;height:220px}
.values p{width:600px;margin:12px auto 18px;color:#4b5563;font-size:12px}
.value-row{display:flex;justify-content:center;gap:34px}
.value{display:flex;align-items:center;gap:8px;font-family:"Montserrat",Arial,sans-serif;font-weight:700;font-size:12px;color:var(--navy);letter-spacing:1px;text-transform:uppercase}
.value i{width:12px;height:12px;border-radius:50%;background:var(--gold);display:inline-block}

/* Footer */
.footer{background:var(--navy);color:#cfd6e2;height:360px;position:relative}
.footer-grid{display:grid;grid-template-columns:280px 160px 320px 1fr;gap:30px;padding:56px 120px 0}
.footer .brand{font-size:22px}
.footer .tag{font-size:10px;color:var(--gold);letter-spacing:2px;margin-top:4px;font-family:"Montserrat",Arial,sans-serif;font-weight:600}
.footer h4{font-family:"Montserrat",Arial,sans-serif;color:var(--gold);font-size:12px;letter-spacing:1.5px;text-transform:uppercase;margin-bottom:14px;white-space:nowrap}
.footer ul{list-style:none}
.footer li{font-size:12px;margin-bottom:6px}
.footer li span{color:var(--gold)}
.social li{display:flex;align-items:center;gap:8px}
.social i{width:8px;height:8px;border-radius:50%;background:var(--gold);display:inline-block}
.footer-bar{position:absolute;left:0;right:0;bottom:0;height:60px;border-top:1px solid rgba(255,255,255,.12);display:flex;align-items:center;justify-content:space-between;padding:0 120px;font-size:11px;color:#9aa6b8}
.footer-bar nav{display:flex;gap:20px}
</style>
</head>
<body>

<header class="hero">
  <div class="hero-photo" role="img" aria-label="Photo of a cleaner in overalls washing large office windows"></div>
  <nav class="nav">
    <div class="brand"><span class="brand-dot"></span>Thornbury Cleaning</div>
    <ul class="menu">
      <li><a class="active" href="#">Home</a></li>
      <li><a href="#">About Us</a></li>
      <li><a href="#">Cleaning Services</a></li>
      <li><a href="#">Contact</a></li>
      <li><a href="#">Service Areas</a></li>
    </ul>
    <div class="nav-call">
      <span class="ico"><svg width="16" height="16" viewBox="0 0 24 24" fill="#fff"><path d="M6.6 10.8a15.1 15.1 0 0 0 6.6 6.6l2.2-2.2a1 1 0 0 1 1-.25 11.4 11.4 0 0 0 3.6.57 1 1 0 0 1 1 1V20a1 1 0 0 1-1 1A17 17 0 0 1 3 4a1 1 0 0 1 1-1h3.5a1 1 0 0 1 1 1c0 1.25.2 2.45.57 3.57a1 1 0 0 1-.25 1z"/></svg></span>
      <div><small>24 hr emergency service</small><strong>Call us: 0412 555 781</strong></div>
    </div>
  </nav>
  <div class="hero-copy">
    <div class="eyebrow">Trusted by locals for three decades</div>
    <h1>30+ Years of Commercial and Residential Cleaning in Sale</h1>
    <p>Whether you manage a busy office or an entire apartment building, you'll meet all the help you can get to keep the space clean.</p>
    <div class="hero-actions">
      <a class="btn btn-gold" href="#">Request a Quote</a>
      <div class="rating">
        <span class="rating-mark"></span>
        <div>
          <div class="stars">
            <svg width="60" height="12" viewBox="0 0 60 12" fill="#f4b400"><path id="s" d="M6 0l1.8 3.8 4.2.5-3.1 2.9.8 4.1L6 9.3 2.3 11.3l.8-4.1L0 4.3l4.2-.5z"/><use href="#s" x="12"/><use href="#s" x="24"/><use href="#s" x="36"/><use href="#s" x="48"/></svg>
          </div>
          <b>Rated 4.9 from 200+ reviews</b>
        </div>
      </div>
    </div>
  </div>
</header>

<section class="partners">
  <div class="label">Organisations we work with</div>
  <div class="partner-row">
    <span class="partner">RLK</span>
    <span class="partner">Bramwell</span>
    <span class="partner">Eastvale Regional Care</span>
    <span class="partner">OPM</span>
    <span class="partner">Lakeside Dental</span>
    <span class="partner">Wellington Homes</span>
    <span class="partner">Riverbend Realty</span>
    <span class="partner">Sale Community Hub</span>
  </div>
</section>

<section class="trust">
  <div class="eyebrow">Trusted by locals for 30 years</div>
  <h2>Call the cleaners you<br>can count on</h2>
  <p class="lead">When you need help cleaning, the last thing you want is more stress. Too often, that's exactly what happens — cleaners don't show up, jobs get rushed or half-done, and you're left wondering why you didn't just do it yourself. You shouldn't have to second-guess whether the job will be done right. You should be able to book it, forget it, and trust it's sorted — properly.</p>
  <p class="note">Trusted by locals for 30+ years to deliver reliable, long-term cleaning — the kind you never have to second-guess.</p>
  <div class="stats">
    <div class="stat">
      <span class="ico"><svg width="24" height="24" viewBox="0 0 24 24" fill="#fff"><circle cx="12" cy="8" r="4"/><path d="M4 21c0-4.4 3.6-7 8-7s8 2.6 8 7z"/></svg></span>
      <h3>Recurring Clients</h3>
      <div class="num">92+</div>
      <p>Homes and businesses who keep us booked week after week, year after year.</p>
    </div>
    <div class="stat">
      <span class="ico"><svg width="24" height="24" viewBox="0 0 24 24" fill="none" stroke="#fff" stroke-width="2"><rect x="3" y="5" width="18" height="16" rx="2"/><path d="M3 10h18M8 3v4M16 3v4"/></svg></span>
      <h3>Visits Per Year</h3>
      <div class="num">4,150+</div>
      <p>Our team is consistently on the road, delivering dependable results on schedule.</p>
    </div>
    <div class="stat">
      <span class="ico"><svg width="24" height="24" viewBox="0 0 24 24" fill="none" stroke="#fff" stroke-width="2"><path d="M3 11l9-7 9 7v10H3z"/><path d="M10 21v-6h4v6"/></svg></span>
      <h3>Pre-Sale / Exit Cleans</h3>
      <div class="num">265+</div>
      <p>Thorough, detail-driven cleans that help properties sell and bonds return.</p>
    </div>
  </div>
</section>

<div class="band-photo cleaner" role="img" aria-label="Photo of a cleaner using a floor scrubbing machine in a bright room"></div>

<section class="services">
  <div class="eyebrow">What we clean</div>
  <h2>Enjoy a spotless environment</h2>
  <div class="cards">
    <article class="card">
      <div class="thumb" role="img" aria-label="Photo of a tidy commercial office"></div>
      <span class="badge"><svg width="22" height="22" viewBox="0 0 24 24" fill="none" stroke="#fff" stroke-width="2"><rect x="5" y="3" width="14" height="18"/><path d="M9 7h2M13 7h2M9 11h2M13 11h2M10 21v-4h4v4"/></svg></span>
      <h3>Commercial Cleaning</h3>
      <p>Offices, medical centres and community spaces cleaned to a steady routine, so your team and visitors walk into a fresh, healthy workplace every day.</p>
      <a class="btn btn-outline" href="#">Learn More</a>
    </article>
    <article class="card featured">
      <div class="thumb home" role="img" aria-label="Photo of a clean, bright living room"></div>
      <span class="badge"><svg width="22" height="22" viewBox="0 0 24 24" fill="none" stroke="#fff" stroke-width="2"><path d="M3 11l9-7 9 7v10H3z"/></svg></span>
      <h3>Residential Cleaning</h3>
      <p>Regular or one-off home cleans that give you back your weekends. Reliable people, the same high standard, and a house that feels calm again.</p>
      <a class="btn btn-outline" href="#">Learn More</a>
    </article>
    <article class="card">
      <div class="thumb window" role="img" aria-label="Photo of clear glass windows being cleaned"></div>
      <span class="badge"><svg width="22" height="22" viewBox="0 0 24 24" fill="none" stroke="#fff" stroke-width="2"><rect x="4" y="3" width="16" height="18"/><path d="M12 3v18M4 12h16"/></svg></span>
      <h3>Window Cleaning</h3>
      <p>Streak-free glass inside and out for homes and shopfronts, letting more light in and leaving a sharp first impression for every visitor.</p>
      <a class="btn btn-outline" href="#">Learn More</a>
    </article>
    <article class="card">
      <div class="thumb steam" role="img" aria-label="Photo of carpet being steam cleaned"></div>
      <span class="badge"><svg width="22" height="22" viewBox="0 0 24 24" fill="none" stroke="#fff" stroke-width="2"><path d="M4 20h16M7 20v-6h10v6M9 10c0-2 2-2 2-4M13 10c0-2 2-2 2-4"/></svg></span>
      <h3>Steam Cleaning</h3>
      <p>Deep carpet and upholstery cleaning that lifts stains, allergens and odours, perfect for end of lease or a seasonal refresh.</p>
      <a class="btn btn-outline" href="#">Learn More</a>
    </article>
  </div>
</section>

<section class="values">
  <div class="eyebrow">Our core values</div>
  <h2>You can trust us to make<br>your space spotless</h2>
  <p>Whether you manage a busy office or a family home, we're here to keep things simple with honest, reliable cleaning you can count on.</p>
  <div class="value-row">
    <span class="value"><i></i>Be Real</span>
    <span class="value"><i></i>Do It Right</span>
    <span class="value"><i></i>Have Fun</span>
    <span class="value"><i></i>Make It Easy</span>
  </div>
</section>

<div class="band-photo vans" role="img" aria-label="Photo of the company's white service vans parked in a row"></div>

<footer class="footer">
  <div class="footer-grid">
    <div>
      <div class="brand"><span class="brand-dot"></span>Thornbury Cleaning</div>
      <div class="tag">SALE, VICTORIA</div>
    </div>
    <div>
      <h4>Quick Links</h4>
      <ul><li>About Us</li><li>Cleaning Services</li><li>Contact Us</li><li>Support</li><li>Service Areas</li></ul>
    </div>
    <div>
      <h4>Contact Us</h4>
      <ul>
        <li>Address: 18 Riverbank Lane,<br>Sale Victoria 3850</li>
        <li><span>ABN:</span> 12 345 678 901</li>
        <li><span>Email:</span> info@thornburycleaning-example.com.au</li>
        <li><span>Phone:</span> 0412 555 781</li>
      </ul>
    </div>
    <div>
      <h4>Stay Social</h4>
      <ul class="social"><li><i></i>Chatter</li><li><i></i>Neighbourly</li><li><i></i>Snapshot</li><li><i></i>WorkNet</li></ul>
    </div>
  </div>
  <div class="footer-bar">
    <span>© 2024 Thornbury Cleaning. All Rights Reserved.</span>
    <nav><span>Privacy Policy</span><span>Terms of Use</span><span>Disclaimer</span><span>Sitemap</span></nav>
  </div>
</footer>

</body>
</html>
```